Business cards for a tribute and obituary website

Our website is called Tribute Lantern.

It is a special place online for people to remember their loved ones who have passed away, through obituaries and tributes. Friends and family can also convey their condolences on the deceased's memorial page. Celebrating the life of the deceased and remembering their legacy is very important to us – death should not be just about grieving.

We would like the card to look tasteful and modern. The design should ideally not have colours that are too bright. The logo and website URL, www.tributelantern.example should be visible on the front of the card, with our slogan "Honouring every life lived" on the back.

The design should communicate our purpose – remembering loved ones who have passed – and also a lighter tone of celebrating life. It should not look like a funeral director's card!

Our logo has been attached. Looking forward to some beautiful designs! Get creative :)
Updates

Project Deadline Extended
Reason: Thank you all for your designs. The rest of my team and I have not reached a decision on which design to select and I am collecting feedback from them. I will provide feedback for any changes that need to be made soon. It would be great if we could see more original designs and in more colours! We will definitely select a design by this deadline.

Industry/Entity Type

Business

Contact Information for Business Card

Wendy Lumb
Project Manager
614772390
wendylumb@tributelantern.example

Font styles to use
Serif
Sans Serif

Requirements
Must have
• Logo and website address (www.tributelantern.example) on the front.
Nice to have
• Hi designers! It would be nice to see alternative colours – feel free to try out colours that are tasteful and subtle. The colour of the business card does not have to be the same as the logo.
• We would also like to see the logo used in different ways, perhaps a glossy or embossed finish. The card should look stylish.

```html
<!DOCTYPE html>
<html lang="en">
<head>
<meta charset="utf-8">
<title>Tribute Lantern – Business Cards</title>
<link rel="stylesheet" href="https://fonts.googleapis.com/css2?family=Bitter:wght@700&family=Libre+Franklin:wght@400&display=swap">
<style>
  :root {
    --navy: #062a48;
    --paper: #f5f7f7;
    --ribbon: #ffffff;
    --backdrop: #e4e4e4;
    --card-shadow: rgba(0, 0, 0, 0.18);
  }
  * { box-sizing: border-box; margin: 0; padding: 0; }
  html, body {
    width: 1200px;
    height: 1000px;
    overflow: hidden;
    background: var(--backdrop);
  }
  .canvas {
    position: relative;
    width: 1200px;
    height: 1000px;
  }
  .card {
    position: absolute;
    left: 250px;
    width: 700px;
    height: 400px;
    box-shadow: 0 6px 18px var(--card-shadow);
    overflow: hidden;
  }

  /* Contact side */
  .card--contact {
    top: 70px;
    background: var(--navy);
    color: var(--paper);
    font-family: "Libre Franklin", Arial, sans-serif;
  }
  .ribbon {
    position: absolute;
    left: 60px;
    top: 0;
    width: 120px;
    height: 270px;
  }
  .ribbon-mark {
    position: absolute;
    left: 60px;
    top: 70px;
    width: 120px;
    text-align: center;
  }
  .ribbon-mark .mark-dot {
    display: block;
    width: 38px;
    height: 38px;
    margin: 0 auto 10px;
    border-radius: 50%;
    background: var(--navy);
  }
  .ribbon-mark .brand-name {
    font-family: "Bitter", Georgia, serif;
    font-weight: 700;
    font-size: 17px;
    line-height: 1.05;
    color: var(--navy);
  }
  .contact {
    position: absolute;
    right: 48px;
    bottom: 40px;
    text-align: right;
    letter-spacing: 0.3px;
  }
  .contact .person-name { font-size: 29px; line-height: 1.1; }
  .contact .person-role { font-size: 15px; margin-bottom: 20px; }
  .contact .detail { font-size: 17px; line-height: 1.35; }

  /* Brand side */
  .card--brand {
    top: 530px;
    background: var(--paper);
    color: var(--navy);
  }
  .brand-lockup {
    position: absolute;
    left: 150px;
    top: 95px;
    display: flex;
    align-items: center;
    gap: 26px;
  }
  .brand-lockup .mark-dot {
    width: 90px;
    height: 90px;
    border-radius: 50%;
    background: var(--navy);
    flex: none;
  }
  .brand-lockup .brand-name {
    font-family: "Bitter", Georgia, serif;
    font-weight: 700;
    font-size: 62px;
    line-height: 0.95;
    color: var(--navy);
  }
  .slogan {
    position: absolute;
    left: 150px;
    top: 290px;
    font-family: "Libre Franklin", Arial, sans-serif;
    font-size: 26px;
    color: var(--navy);
  }
</style>
</head>
<body>
<main class="canvas">

  <section class="card card--contact" aria-label="Business card, contact side">
    <svg class="ribbon" viewBox="0 0 120 270" aria-hidden="true">
      <polygon points="0,0 120,0 120,270 60,225 0,270" fill="var(--ribbon)"/>
    </svg>
    <div class="ribbon-mark">
      <span class="mark-dot"></span>
      <div class="brand-name">Tribute<br>Lantern</div>
    </div>
    <div class="contact">
      <p class="person-name">Wendy Lumb</p>
      <p class="person-role">Project Manager</p>
      <p class="detail">614772390</p>
      <p class="detail">wendylumb@tributelantern.example</p>
      <p class="detail">www.tributelantern.example</p>
    </div>
  </section>

  <section class="card card--brand" aria-label="Business card, brand side">
    <div class="brand-lockup">
      <span class="mark-dot"></span>
      <div class="brand-name">Tribute<br>Lantern</div>
    </div>
    <p class="slogan">Honouring every life lived</p>
  </section>

</main>
</body>
</html>
```